Flyer Design Project

We are a coaching organisation that is about to launch classes catering to local and international university students in Australia. We would like a flyer that is fresh, captivating and ultimately pushes people to our website.
To understand the artistic approach to our business, visit our website: www.brightlanetutors.com.au
Updates
Hi designers, we have changed the criteria slightly to give you more creative license... Feel free to ask any questions, all the best.
Target Market(s)
International University Students aged between 18-25
Industry/Entity Type
University
Requirements
Must have
- Size: 1 sided A5 flyer
Must have logo on page
Introductory offer of 20% off all courses
Bright Lane Tutors exists to help university students with real life skill development such as public speaking. We aim to equip students with skills that are not taught in the university environment to enable them to maximise their results.
To find out more visit: www.brightlanetutors.com.au
CONTACT DETAILS: Leave space for 10 digit phone number
Nice to have
- Bold, eye catching design
Fresh, fun and professional look
Good use of typography
Should not have
- Do not use colours outside or that do not compliment our colour palette. You can view our three main colours (blue, pink, yellow) on our website.
www.brightlanetutors.com.au/courses/publicspeaking

```html
<!DOCTYPE html>
<html lang="en">
<head>
<meta charset="utf-8">
<title>Bright Lane Tutors – Flyer</title>
<link href="https://fonts.googleapis.com/css2?family=Source+Sans+3:wght@400;600;700&display=swap" rel="stylesheet">
<style>
:root{
  --blue:#29b1e6;
  --navy:#1a4f9c;
  --pink:#e8426f;
  --yellow:#fbe66e;
  --orange:#ec7a23;
  --green:#3db56a;
  --ink:#231f20;
  --text:#555659;
  --rule:#d9d9d9;
  --white:#ffffff;
}
*{margin:0;padding:0;box-sizing:border-box}
html,body{width:877px;height:1200px;overflow:hidden;background:var(--white)}
body{font-family:"Source Sans 3",Arial,sans-serif;color:var(--text)}
.flyer{position:relative;width:877px;height:1200px;overflow:hidden;background:var(--white)}

.brand{position:absolute;left:42px;top:70px;display:flex;align-items:center;gap:24px}
.brand-dot{width:76px;height:76px;border-radius:50%;background:var(--blue)}
.brand-name{font-size:64px;font-weight:600;line-height:1;color:var(--navy);letter-spacing:-0.5px}

.offer{position:absolute;left:566px;top:66px;width:286px;height:286px;border-radius:50%;
  background:var(--blue);color:var(--white);text-align:center;display:flex;flex-direction:column;
  justify-content:center;font-size:30px;line-height:1.12}
.offer strong{font-size:52px;font-weight:700;line-height:1.05}

.intro{position:absolute;left:35px;top:240px;font-size:24px;line-height:37px;white-space:nowrap}
.intro b{font-weight:700}

.courses{position:absolute;left:25px;top:458px;width:827px;border-collapse:collapse;
  table-layout:fixed;text-align:center;font-size:21px}
.courses th{height:48px;font-size:21px;font-weight:700;color:var(--white)}
.courses th.hd{background:var(--ink)}
.courses th.intensive{background:var(--blue)}
.courses th.essentials{background:var(--pink)}
.courses th.tuning{background:var(--yellow)}
.courses td{border:1px solid var(--rule);height:42px}
.courses tr.skills td{height:276px;vertical-align:top;padding-top:8px}
.courses tr.extra td{height:40px}
.skill-stack{display:flex;flex-direction:column;align-items:center;gap:12px}

.tag{display:inline-flex;flex:none;width:31px;height:31px;border-radius:3px;align-items:center;justify-content:center;
  font-size:17px;font-weight:700;color:var(--white)}
.tag.fe{background:var(--blue)}
.tag.cc{background:var(--orange)}
.tag.pp{background:var(--pink)}
.tag.ft{background:var(--yellow)}
.tag.im{background:var(--green)}
.tag.gr{background:var(--ink)}
.none{width:31px;height:31px}

.band{position:absolute;left:0;top:0}

.legend{position:absolute;left:68px;top:950px;display:grid;grid-template-columns:187px 207px 200px;row-gap:26px}
.legend-item{display:flex;align-items:center;gap:12px;font-size:18px;color:var(--text)}
.legend-label{text-transform:uppercase}

.contact{position:absolute;left:33px;top:1098px;color:var(--white)}
.contact-label{font-size:23px;line-height:1}
.contact-phone{font-size:34px;font-weight:700;margin-top:14px;line-height:1}
.divider{position:absolute;left:262px;top:1088px;width:2px;height:84px;background:var(--white)}
.web{position:absolute;left:287px;top:1098px;color:var(--white)}
.web-label{font-size:23px;line-height:1}
.web-url{font-size:34px;font-weight:700;margin-top:14px;line-height:1}
</style>
</head>
<body>
<div class="flyer">

  <div class="brand">
    <span class="brand-dot"></span>
    <span class="brand-name">Bright Lane<br>Tutors</span>
  </div>

  <div class="offer">
    <span>Introductory<br>offer of</span>
    <strong>20% off</strong>
    <span>all courses</span>
  </div>

  <p class="intro"><b>Bright Lane Tutors</b> exists to help university<br>students with real life skill development such as<br><b>PUBLIC SPEAKING</b>. We aim to equip students with<br>skills that are not taught in the university environment to<br>enable them to maximise their results.</p>

  <table class="courses">
    <thead>
      <tr>
        <th class="hd">HD Package</th>
        <th class="intensive">One Day Intensive</th>
        <th class="essentials">Uni Essentials</th>
        <th class="tuning">Fine Tuning</th>
      </tr>
    </thead>
    <tbody>
      <tr><td>$300</td><td>$400</td><td>$250</td><td>$200</td></tr>
      <tr><td>5 x 1hr classes</td><td>Full day course</td><td>3 x 1hr classes</td><td>2 x 1hr classes</td></tr>
      <tr class="skills">
        <td><div class="skill-stack">
          <span class="tag fe">Fe</span><span class="tag cc">Cc</span><span class="tag pp">Pp</span>
          <span class="tag ft">Ft</span><span class="tag im">Im</span><span class="tag gr">Gr</span>
        </div></td>
        <td><div class="skill-stack">
          <span class="tag fe">Fe</span><span class="tag cc">Cc</span><span class="tag pp">Pp</span>
          <span class="tag ft">Ft</span><span class="tag im">Im</span><span class="tag gr">Gr</span>
        </div></td>
        <td><div class="skill-stack">
          <svg class="none" viewBox="0 0 31 31"><path d="M5 5L26 26M26 5L5 26" stroke="#c8c8c8" stroke-width="2"/></svg>
          <span class="tag cc">Cc</span><span class="tag pp">Pp</span><span class="tag ft">Ft</span>
          <svg class="none" viewBox="0 0 31 31"><path d="M5 5L26 26M26 5L5 26" stroke="#c8c8c8" stroke-width="2"/></svg>
          <svg class="none" viewBox="0 0 31 31"><path d="M5 5L26 26M26 5L5 26" stroke="#c8c8c8" stroke-width="2"/></svg>
        </div></td>
        <td><div class="skill-stack">
          <svg class="none" viewBox="0 0 31 31"><path d="M5 5L26 26M26 5L5 26" stroke="#c8c8c8" stroke-width="2"/></svg>
          <svg class="none" viewBox="0 0 31 31"><path d="M5 5L26 26M26 5L5 26" stroke="#c8c8c8" stroke-width="2"/></svg>
          <svg class="none" viewBox="0 0 31 31"><path d="M5 5L26 26M26 5L5 26" stroke="#c8c8c8" stroke-width="2"/></svg>
          <span class="tag ft">Ft</span><span class="tag im">Im</span>
          <svg class="none" viewBox="0 0 31 31"><path d="M5 5L26 26M26 5L5 26" stroke="#c8c8c8" stroke-width="2"/></svg>
        </div></td>
      </tr>
      <tr class="extra"><td colspan="4">+ Free public speaking guide</td></tr>
    </tbody>
  </table>

  <svg class="band" width="877" height="1200" viewBox="0 0 877 1200" aria-hidden="true">
    <path d="M0 1062 C260 1100 620 1060 877 925 L877 1200 L0 1200 Z" fill="#29b1e6"/>
  </svg>

  <div class="legend">
    <div class="legend-item"><span class="tag fe">Fe</span><span class="legend-label">Fear</span></div>
    <div class="legend-item"><span class="tag pp">Pp</span><span class="legend-label">Power Point</span></div>
    <div class="legend-item"><span class="tag im">Im</span><span class="legend-label">Impact</span></div>
    <div class="legend-item"><span class="tag cc">Cc</span><span class="legend-label">Cue Cards</span></div>
    <div class="legend-item"><span class="tag ft">Ft</span><span class="legend-label">Fine Tuning</span></div>
    <div class="legend-item"><span class="tag gr">Gr</span><span class="legend-label">Groups</span></div>
  </div>

  <div class="contact">
    <div class="contact-label">CONTACT US NOW!</div>
    <div class="contact-phone">09876 54321</div>
  </div>
  <div class="divider"></div>
  <div class="web">
    <div class="web-label">To find out more visit:</div>
    <div class="web-url">www.brightlanetutors.com.au</div>
  </div>

</div>
</body>
</html>
```